Sales Flyer for Outdoor Kitchens

Looks to have a trifold flyer designed based off website content / projects. Use www.brickleafyardworks.com for content

```html
<!DOCTYPE html>
<html lang="en">
<head>
<meta charset="utf-8">
<title>Brickleaf Yardworks – Trifold Flyer</title>
<link href="https://fonts.googleapis.com/css2?family=Montserrat:wght@400;500;600;700;800&display=swap" rel="stylesheet">
<style>
:root{
  --stage:#3a3a3a;
  --green:#3bb54a;
  --green-dark:#2c9a3c;
  --blue:#1f9ad6;
  --blue-deep:#1b6fb5;
  --ink:#2f3b48;
  --body:#4a4f55;
  --white:#ffffff;
  --mist:#eef1f3;
}
*{margin:0;padding:0;box-sizing:border-box}
html,body{width:900px;height:1200px;overflow:hidden;background:var(--stage)}
body{position:relative;font-family:"Montserrat",Arial,sans-serif;color:var(--body)}
.sheet{position:absolute;overflow:hidden;background:var(--white);box-shadow:0 6px 18px rgba(0,0,0,.35)}
.sheet-front{left:66px;top:52px;width:708px;height:500px}
.sheet-inside{left:122px;top:640px;width:714px;height:503px}
.sheet-art{position:absolute;left:0;top:0;width:100%;height:100%}
.abs{position:absolute}
.side-label{position:absolute;font-weight:800;font-size:32px;letter-spacing:2px;color:var(--green);transform:rotate(-90deg);transform-origin:center}
.label-front{left:760px;top:404px;width:110px;text-align:center}
.label-inside{left:12px;top:1026px;width:140px;text-align:center}

/* process panel */
.process{left:0;top:0;width:236px;padding:14px 14px 0 22px;color:var(--white)}
.kicker{font-size:6px;font-weight:700;letter-spacing:1px;text-align:center;display:flex;align-items:center;justify-content:center;gap:5px}
.kicker::before,.kicker::after{content:"";width:18px;height:1px;background:currentColor}
.process-title{font-size:13px;font-weight:600;text-align:center;letter-spacing:.5px;margin:2px 0 10px}
.step{margin-bottom:7px}
.step-name{font-size:7.5px;font-weight:700;position:relative;padding-left:6px}
.step-name::before{content:"";position:absolute;left:-7px;top:2px;width:4px;height:4px;border-radius:50%;background:var(--white)}
.step-text{font-size:7px;line-height:1.3;padding-left:6px;margin-top:2px}

/* call block */
.call{left:280px;top:22px;display:flex;align-items:center;gap:8px}
.call-icon{width:24px;height:24px;border-radius:50%;background:var(--green);display:flex;align-items:center;justify-content:center}
.call-small{font-size:8px;font-weight:600;color:var(--ink)}
.call-number{font-size:14px;font-weight:600;color:var(--ink);line-height:1.1}
.cta{left:272px;top:56px;width:165px;height:19px;background:var(--green);color:var(--white);font-size:8.5px;font-weight:500;display:flex;align-items:center;justify-content:center;border-radius:2px;letter-spacing:.3px}

/* brand */
.brand{display:flex;align-items:center;gap:5px;font-weight:800;color:var(--green);white-space:nowrap}
.brand-dot{border-radius:50%;background:var(--blue)}
.brand-main{left:524px;top:30px;font-size:11px}
.brand-main .brand-dot{width:12px;height:12px}
.brand-small{left:250px;top:440px;font-size:6.5px}
.brand-small .brand-dot{width:8px;height:8px}

/* contact */
.contact-title{left:262px;top:392px;width:180px;font-size:12px;font-weight:700;color:var(--blue-deep);display:flex;align-items:center;justify-content:center;gap:6px}
.contact-title::before,.contact-title::after{content:"";width:26px;height:2px;background:var(--blue-deep)}
.contact-row{left:318px;display:flex;gap:6px;font-size:7px;color:var(--ink);line-height:1.35}
.contact-row svg{flex:none;margin-top:1px}

/* headline */
.headline{left:480px;top:372px;width:216px;text-align:center;font-weight:700;font-size:21px;line-height:1.22}
.headline .hl-blue{color:var(--blue-deep)}
.headline .hl-green{color:var(--green)}
.hl-first{display:flex;align-items:center;justify-content:center;gap:6px}
.hl-first::before,.hl-first::after{content:"";width:26px;height:2px;background:var(--blue-deep)}

/* inside */
.about{left:18px;top:222px;width:205px;color:var(--white)}
.section-title{font-size:14px;font-weight:600;color:var(--ink);text-align:center;letter-spacing:.5px;margin:1px 0 8px}
.about-text{font-size:7.3px;line-height:1.35}
.services{left:18px;top:346px;width:205px;color:var(--white)}
.service-lead{font-size:7px;margin-top:-2px}
.service{position:absolute;display:flex;gap:7px}
.thumb{flex:none;border-radius:5px}
.service-name{font-size:7px;font-weight:700;margin-bottom:3px;letter-spacing:.2px}
.service-text{font-size:6.8px;line-height:1.32}
.svc-left{left:18px;top:404px;width:205px;color:var(--white)}
.svc-mid .service-name{color:var(--green)}
.svc-mid .service-text{color:var(--ink)}
.svc-right{color:var(--white)}
</style>
</head>
<body>

<div class="side-label label-front">FRONT</div>
<div class="side-label label-inside">INSIDE</div>

<!-- FRONT SHEET -->
<section class="sheet sheet-front">
  <svg class="sheet-art" viewBox="0 0 708 500" aria-hidden="false">
    <defs>
      <linearGradient id="fGreen" x1="0" y1="0" x2="0" y2="1"><stop offset="0" stop-color="#3cb64b"/><stop offset="1" stop-color="#2e9d3f"/></linearGradient>
      <linearGradient id="fPavilion" x1="0" y1="0" x2="0" y2="1"><stop offset="0" stop-color="#6f9a5a"/><stop offset=".35" stop-color="#4c7a38"/><stop offset=".6" stop-color="#8a5a3a"/><stop offset="1" stop-color="#5e9a3c"/></linearGradient>
      <linearGradient id="fFire" x1="0" y1="0" x2="0" y2="1"><stop offset="0" stop-color="#6d5646"/><stop offset=".5" stop-color="#b07a4c"/><stop offset="1" stop-color="#8c6a55"/></linearGradient>
      <linearGradient id="fFade" x1="0" y1="0" x2="1" y2="0"><stop offset="0" stop-color="#e6eaec"/><stop offset="1" stop-color="#f4f6f7"/></linearGradient>
    </defs>
    <rect width="708" height="500" fill="var(--mist)"/>
    <rect x="236" y="330" width="472" height="170" fill="url(#fFade)" role="img" aria-label="Faded photo of a covered backyard pavilion"/>
    <path d="M236,80 H708 V335 Q560,360 420,372 Q320,378 236,362 Z" fill="url(#fPavilion)" role="img" aria-label="Photo of a wooden pavilion with brick columns on a green lawn under oak trees"/>
    <path d="M236,362 Q320,378 420,372 Q560,360 708,335" fill="none" stroke="var(--blue)" stroke-width="4"/>
    <rect x="236" y="0" width="472" height="86" fill="#ffffff"/>
    <ellipse cx="600" cy="14" rx="114" ry="72" fill="#ffffff" stroke="var(--green)" stroke-width="4"/>
    <path d="M0,316 Q120,330 236,350 V500 H0 Z" fill="url(#fFire)" role="img" aria-label="Photo of a round stone fire pit with seating wall at dusk"/>
    <path d="M0,0 H236 V350 Q120,330 0,316 Z" fill="url(#fGreen)"/>
    <path d="M0,316 Q120,330 236,350" fill="none" stroke="var(--blue)" stroke-width="4"/>
  </svg>

  <div class="abs process">
    <div class="kicker">WHAT WE DO</div>
    <div class="process-title">EFFECTIVE PROCESS</div>
    <div class="step"><div class="step-name">TELL US ABOUT YOUR PROJECT</div><div class="step-text">This is where you can share your ideas of your dream backyard with us.</div></div>
    <div class="step"><div class="step-name">PHONE CONSULTATION</div><div class="step-text">Upon review of your project information plan, we will give you a call to discuss your plans, budgets &amp; timelines.</div></div>
    <div class="step"><div class="step-name">IN-PERSON CONSULTATION</div><div class="step-text">We will visit you at your location and walk through your space to better understand your visions.</div></div>
    <div class="step"><div class="step-name">DESIGN</div><div class="step-text">The majority of HOA &amp; municipalities in our area require at least a conceptual plan and construction drawings. We offer an independently contracted design phase for this portion of a project.</div></div>
    <div class="step"><div class="step-name">CONSTRUCTION</div><div class="step-text">A pre-construction kick off meeting will take place on-site to ensure expectations are aligned.</div></div>
    <div class="step"><div class="step-name">POST CONSTRUCTION WALKTHROUGH</div><div class="step-text">Upon completion of your project, the owner of BYW will perform a job site walk with you to ensure everything was completed per the job specifications.</div></div>
  </div>

  <div class="abs call">
    <div class="call-icon"><svg width="13" height="13" viewBox="0 0 24 24"><path fill="#fff" d="M6.6 10.8a15.1 15.1 0 0 0 6.6 6.6l2.2-2.2c.3-.3.7-.4 1-.2 1.1.4 2.3.6 3.6.6.6 0 1 .4 1 1V20c0 .6-.4 1-1 1C10.6 21 3 13.4 3 4c0-.6.4-1 1-1h3.5c.6 0 1 .4 1 1 0 1.3.2 2.5.6 3.6.1.3 0 .7-.2 1z"/></svg></div>
    <div><div class="call-small">Call Us Now</div><div class="call-number">281-555-0148</div></div>
  </div>
  <div class="abs cta">REQUEST CONSULTATION</div>

  <div class="abs brand brand-main"><span class="brand-dot"></span>BRICKLEAF YARDWORKS</div>

  <div class="abs contact-title">CONTACT US</div>
  <div class="abs brand brand-small"><span class="brand-dot"></span>BRICKLEAF<br>YARDWORKS</div>
  <div class="abs contact-row" style="top:424px">
    <svg width="7" height="9" viewBox="0 0 24 30"><path fill="var(--green)" d="M12 0C5.4 0 0 5.4 0 12c0 9 12 18 12 18s12-9 12-18C24 5.4 18.6 0 12 0zm0 17a5 5 0 1 1 0-10 5 5 0 0 1 0 10z"/></svg>
    <span>4820 Cedar Hollow Rd Ste 210 PMB<br>3391 Rosenberg, 77471, US</span>
  </div>
  <div class="abs contact-row" style="top:451px">
    <svg width="8" height="8" viewBox="0 0 24 24"><path fill="var(--green)" d="M6.6 10.8a15.1 15.1 0 0 0 6.6 6.6l2.2-2.2c.3-.3.7-.4 1-.2 1.1.4 2.3.6 3.6.6.6 0 1 .4 1 1V20c0 .6-.4 1-1 1C10.6 21 3 13.4 3 4c0-.6.4-1 1-1h3.5c.6 0 1 .4 1 1 0 1.3.2 2.5.6 3.6.1.3 0 .7-.2 1z"/></svg>
    <span>281-555-0148</span>
  </div>
  <div class="abs contact-row" style="top:469px">
    <svg width="9" height="7" viewBox="0 0 24 18"><path fill="var(--green)" d="M0 0h24v18H0z"/><path d="M0 0l12 9 12-9" fill="none" stroke="#fff" stroke-width="2"/></svg>
    <span>hello@brickleafyardworks.com</span>
  </div>

  <div class="abs headline">
    <div class="hl-blue hl-first">Create</div>
    <div class="hl-green">YOUR DREAM</div>
    <div class="hl-green">BACKYARD</div>
    <div class="hl-blue">With Us</div>
  </div>
</section>

<!-- INSIDE SHEET -->
<section class="sheet sheet-inside">
  <svg class="sheet-art" viewBox="0 0 714 503">
    <defs>
      <linearGradient id="iPavilion" x1="0" y1="0" x2="0" y2="1"><stop offset="0" stop-color="#8a5630"/><stop offset=".3" stop-color="#5f8f45"/><stop offset=".7" stop-color="#6d6a5c"/><stop offset="1" stop-color="#8b6a58"/></linearGradient>
      <linearGradient id="iBlue" x1="0" y1="0" x2="0" y2="1"><stop offset="0" stop-color="#23a2dd"/><stop offset="1" stop-color="#1d8fcc"/></linearGradient>
      <linearGradient id="iGreen" x1="0" y1="0" x2="0" y2="1"><stop offset="0" stop-color="#3cb64b"/><stop offset="1" stop-color="#2e9d3f"/></linearGradient>
      <linearGradient id="iCabana" x1="0" y1="0" x2="0" y2="1"><stop offset="0" stop-color="#8fa9b5"/><stop offset=".45" stop-color="#e9e6e0"/><stop offset="1" stop-color="#7a5a44"/></linearGradient>
    </defs>
    <rect width="714" height="503" fill="#ffffff"/>
    <path d="M0,0 H714 V160 Q560,212 360,215 Q160,214 0,180 Z" fill="url(#iPavilion)" role="img" aria-label="Photo of a cedar pavilion with outdoor lounge seating, fire table and ceiling fans"/>
    <path d="M238,212 Q300,215 360,215 Q420,215 476,207" fill="none" stroke="var(--green)" stroke-width="5"/>
    <path d="M0,180 Q120,205 238,212 V503 H0 Z" fill="url(#iBlue)"/>
    <path d="M476,207 Q600,195 714,160 V503 H476 Z" fill="url(#iGreen)"/>
    <path d="M476,503 V372 Q560,302 714,312 V503 Z" fill="url(#iCabana)" stroke="#ffffff" stroke-width="4" role="img" aria-label="Photo of a white-roofed cabana with outdoor dining set"/>
    <path d="M478,366 Q560,296 714,306" fill="none" stroke="var(--blue)" stroke-width="4"/>
  </svg>

  <div class="abs about">
    <div class="kicker">ABOUT US</div>
    <div class="section-title">WHO WE ARE</div>
    <p class="about-text">With over a decade of experience in the industry, Dale Whitcomb, the owner and operator of BYW, has become a well-known name in the Houston area. His passion for outdoor living spaces, coupled with his keen eye for design and attention to detail, has led him to create some of the most stunning and functional outdoor spaces for his clients.</p>
  </div>

  <div class="abs services">
    <div class="kicker">WHAT WE DO</div>
    <div class="section-title">SERVICES</div>
    <p class="service-lead">We perform complete turnkey services</p>
  </div>

  <div class="service svc-left">
    <svg class="thumb" width="80" height="75"><rect width="80" height="75" rx="5" fill="#8a6a50" role="img" aria-label="Photo of a brick outdoor kitchen with grill"/></svg>
    <div><div class="service-name">OUTDOOR KITCHENS</div><div class="service-text">We redefine outdoor living by bringing the heart of your home outdoors. Our focus on outdoor kitchens goes beyond functionality – we create immersive culinary spaces that elevate your outdoor living experience</div></div>
  </div>

  <div class="service svc-mid" style="left:243px;top:237px;width:228px">
    <svg class="thumb" width="87" height="75"><rect width="87" height="75" rx="5" fill="#b7b3a8" role="img" aria-label="Photo of a white pavilion over a patio dining area"/></svg>
    <div><div class="service-name">PAVILIONS, PATIOS &amp; PERGOLAS</div><div class="service-text">Discover the beauty and versatility of our pergolas and patio covers, designed to bring serenity to your backyard. We specialize in creating outdoor spaces that seamlessly blend elegance, functionality, and tranquility</div></div>
  </div>
  <div class="service svc-mid" style="left:243px;top:320px;width:228px">
    <svg class="thumb" width="87" height="75"><rect width="87" height="75" rx="5" fill="#8d6c55" role="img" aria-label="Photo of a stone fire pit on a patio"/></svg>
    <div><div class="service-name">FIRE PITS</div><div class="service-text">We transform ordinary outdoor spaces into extraordinary havens of warmth and ambiance. Our focus on outdoor fire features brings a touch of magic to your backyard, creating a space that invites relaxation, entertainment, and lasting memories.</div></div>
  </div>
  <div class="service svc-mid" style="left:243px;top:403px;width:228px">
    <svg class="thumb" width="87" height="75"><rect width="87" height="75" rx="5" fill="#5aa6c8" role="img" aria-label="Photo of a backyard swimming pool"/></svg>
    <div><div class="service-name">POOLS</div><div class="service-text">Our expert team will create a customized plan that brings together your vision and practicality, resulting in a beautiful and functional pool that perfectly complements your outdoor space.</div></div>
  </div>

  <div class="service svc-right" style="left:482px;top:228px;width:222px">
    <svg class="thumb" width="86" height="75"><rect width="86" height="75" rx="5" fill="#3e5a34" role="img" aria-label="Photo of lit garden landscaping at night"/></svg>
    <div><div class="service-name">LANDSCAPING &amp; LIGHTING</div><div class="service-text">Design a captivating backyard oasis with our landscaping and lighting service, harmonizing lush landscapes and illumination for a beautiful outdoor space.</div></div>
  </div>
</section>

</body>
</html>
```